Ad for regional magazine for startup "Varomek"

We need a small ad for a small German regional magazine for our startup company Varomek which provides on-premise service for all kind of electronic problems.

We also need the Indesign files to be able to make minor changes (e.g. the phone number) in the future.

An example ad that we used before (for another region with another phone number) is attached.

Industry/Entity Type

Technical Service

Requirements
Must have
• Needed contents:
• "Elektronik-Problem?" (Electronic problem?)
• "Ihr Media-Pannenhelfer kommt" (Your media helper comes)
• "TV, Video, Telefon, Smartphone, Internet, Computer"
• "Terminbuchung: 07051-3920648" (booking)
• "Soforthilfe - auch abends und am Wochenende" (immediate help - also in the evenings and at the weekend)
• "www.varomek.de"
• logo
• picture
• Size: 90mm (width) x 50-70mm (height)
• Font & colors: see attachment

```html
<!DOCTYPE html>
<html lang="de">
<head>
<meta charset="utf-8">
<title>Varomek – Anzeige</title>
<link rel="stylesheet" href="https://fonts.googleapis.com/css2?family=Fira+Sans:ital,wght@0,400;0,500;0,700;1,400;1,500&family=Fira+Sans+Condensed:wght@400&display=swap">
<style>
  :root {
    --slate: #4a5256;
    --green: #5cb346;
    --white: #ffffff;
    --rule: #6d7477;
    --photo-light: #f1ece4;
    --photo-mid: #d9cbb5;
    --photo-dark: #b8a98f;
  }
  html, body {
    margin: 0;
    padding: 0;
    width: 1200px;
    height: 982px;
    overflow: hidden;
    background: var(--white);
  }
  .ad {
    position: relative;
    width: 1200px;
    height: 982px;
    font-family: "Fira Sans", Arial, sans-serif;
    color: var(--slate);
  }
  .ad-frame {
    position: absolute;
    left: 0;
    top: 0;
  }
  .headline {
    position: absolute;
    left: 108px;
    width: 982px;
    top: 158px;
    margin: 0;
    text-align: center;
    font-weight: 700;
    font-size: 80px;
    line-height: 1;
    color: var(--green);
  }
  .subline {
    position: absolute;
    left: 108px;
    width: 982px;
    top: 252px;
    margin: 0;
    text-align: center;
    font-weight: 400;
    font-size: 40px;
    letter-spacing: 4.3px;
    line-height: 1;
    color: var(--white);
  }
  .service-photo {
    position: absolute;
    left: 108px;
    top: 320px;
    width: 697px;
    height: 325px;
    background: linear-gradient(100deg, var(--photo-light) 0%, #e8e2d8 35%, var(--photo-mid) 70%, var(--photo-dark) 100%);
  }
  .service-list {
    position: absolute;
    left: 836px;
    top: 337px;
    width: 209px;
    margin: 0;
    padding: 0;
    list-style: none;
    font-family: "Fira Sans Condensed", "Arial Narrow", sans-serif;
    font-size: 31px;
    line-height: 1;
    text-align: center;
    color: #1e2224;
  }
  .service-list li {
    height: 55.5px;
    box-sizing: border-box;
    padding-top: 2px;
    border-bottom: 2px solid var(--rule);
    margin-bottom: 1px;
  }
  .service-list li:last-child {
    border-bottom: none;
  }
  .availability {
    position: absolute;
    left: 160px;
    top: 655px;
    margin: 0;
    font-style: italic;
    font-size: 26px;
    letter-spacing: 1.2px;
    color: var(--slate);
  }
  .website {
    position: absolute;
    left: 645px;
    top: 708px;
    margin: 0;
    font-style: italic;
    font-weight: 500;
    font-size: 36px;
    letter-spacing: 1.5px;
    color: var(--slate);
  }
  .booking {
    position: absolute;
    right: 655px;
    top: 755px;
    text-align: right;
    color: var(--slate);
  }
  .booking-label {
    display: block;
    font-size: 33px;
    line-height: 1;
  }
  .booking-phone {
    display: block;
    margin-top: 8px;
    font-weight: 700;
    font-size: 42px;
    letter-spacing: 2px;
    line-height: 1;
  }
  .brand {
    position: absolute;
    left: 572px;
    top: 752px;
    display: flex;
    align-items: center;
    gap: 18px;
  }
  .brand-name {
    font-weight: 700;
    font-size: 92px;
    line-height: 1;
    letter-spacing: 2px;
    color: var(--slate);
  }
  .brand-dot {
    width: 26px;
    height: 26px;
    background: var(--green);
    margin-top: 30px;
  }
</style>
</head>
<body>
<div class="ad">
  <svg class="ad-frame" width="1200" height="982" viewBox="0 0 1200 982" aria-hidden="true">
    <path class="header-band" fill="#4a5256"
      d="M108 222 A112 112 0 0 1 220 110 L990 110 A100 100 0 0 1 1090 210 L1090 320 L108 320 Z"/>
    <path class="side-frame" fill="#4a5256"
      d="M572 872 L990 872 A100 100 0 0 0 1090 772 L1090 320 L1075 320 L1075 772 A86 86 0 0 1 989 858 L572 858 Z"/>
  </svg>

  <h1 class="headline">Elektronik-Problem?</h1>
  <p class="subline">IHR MEDIA-PANNENHELFER KOMMT</p>

  <div class="service-photo" role="img" aria-label="Foto: Servicetechniker erklärt einem älteren Kunden am Küchentisch ein Tablet"></div>

  <ul class="service-list">
    <li>TELEVISION</li>
    <li>VIDEO</li>
    <li>TELEFON</li>
    <li>SMARTPHONE</li>
    <li>INTERNET</li>
    <li>COMPUTER</li>
  </ul>

  <p class="availability">Soforthilfe - auch abends und am Wochenende</p>

  <p class="website">www.varomek.de</p>

  <div class="booking">
    <span class="booking-label">TERMINBUCHUNG</span>
    <span class="booking-phone">07051-3920648</span>
  </div>

  <div class="brand">
    <span class="brand-name">Varomek</span>
    <span class="brand-dot"></span>
  </div>
</div>
</body>
</html>
```